RESIDENCE VALBRUNETTE

The CORVALIS Immobilier company exclusively offers apartments for sale under a tax exemption law (BRESSAUTINIÉ) in CAMBRAI, 92 apartments are available, fully renovated with balcony, terrace, elevator, in a former military residence known to the city.
We want to make a book to give to our customers.

```html
<!DOCTYPE html>
<html lang="fr">
<head>
<meta charset="utf-8">
<title>Loi Bressautinié – Les conditions à respecter</title>
<link href="https://fonts.googleapis.com/css2?family=Crimson+Text:wght@400;600&display=swap" rel="stylesheet">
<style>
  :root {
    --backdrop: #000000;
    --paper: #ffffff;
    --ink: #111111;
    --icon: #3a3f47;
    --photo-tone: #b07a66;
    --photo-edge: #666666;
  }
  * { margin: 0; padding: 0; box-sizing: border-box; }
  html, body {
    width: 1200px; height: 675px; overflow: hidden;
    background: var(--backdrop);
    font-family: "Crimson Text", Georgia, serif;
    color: var(--ink);
  }
  .spread {
    position: absolute; left: 8px; top: 129px;
    width: 1184px; height: 417px;
    background: var(--paper);
  }
  .page { position: absolute; top: 0; height: 100%; }
  .page--left { left: 0; width: 592px; }
  .page--right { left: 592px; width: 592px; }

  .info-icon { position: absolute; left: 68px; top: 165px; width: 78px; height: 78px; }
  .conditions { position: absolute; left: 171px; top: 155px; width: 332px; }
  .conditions__title {
    font-weight: 400; font-size: 22px; line-height: 1.1;
    letter-spacing: -0.1px; margin-bottom: 16px;
  }
  .conditions__text { font-size: 8.1px; line-height: 10.2px; }

  .folio {
    position: absolute; top: 400px; font-size: 6.4px; letter-spacing: 0.1px;
  }
  .page--left .folio { left: 25px; }
  .page--right .folio { right: 26px; }

  .building-photo {
    position: absolute; left: 0; top: 0; width: 163px; height: 100%;
    background: var(--photo-tone);
    border-left: 1px solid var(--photo-edge);
  }
  .advice { position: absolute; left: 172px; font-size: 8.1px; line-height: 10.2px; white-space: nowrap; }
</style>
</head>
<body>
  <div class="spread">
    <section class="page page--left">
      <svg class="info-icon" viewBox="0 0 78 78" aria-hidden="true">
        <circle cx="39" cy="39" r="36" fill="none" stroke="var(--icon)" stroke-width="4"/>
        <circle cx="39" cy="21" r="4.2" fill="var(--icon)"/>
        <path d="M33 31h9v22h4v4H32v-4h4V35h-3z" fill="var(--icon)"/>
      </svg>
      <div class="conditions">
        <h1 class="conditions__title">Les conditions à respecter</h1>
        <p class="conditions__text">Aucune reprise de l’avantage fiscal acquis n’est effectuée en cas d’invalidité correspondant au classement dans la deuxième ou la troisième des catégories prévues à l’article L. 341-4 du code de la sécurité sociale, de licenciement ou de décès du contribuable ou de l’un des membres du couple soumis à imposition commune.</p>
      </div>
      <p class="folio">LOI BRESSAUTINIÉ // 12</p>
    </section>

    <section class="page page--right">
      <div class="building-photo" role="img" aria-label="Photo de la résidence en brique"></div>
      <p class="advice" style="top:60px">Investir en toute sécurité</p>
      <p class="advice" style="top:80px">Conseils pour investir en loi Bressautinié</p>
      <p class="advice" style="top:100px">Perte du bénéfice de la réduction d’impôt Logement non loué<br>Passage notaire en n+1Hausse des taux d’emprunt</p>
      <p class="advice" style="top:130px">la-loi-bressautinie.net</p>
      <p class="advice" style="top:211px">AFIN DE PARER À CES RISQUES EVENTUELS</p>
      <p class="advice" style="top:231px">Faites vous aider par un professionnel : prenez rendez-vous gratuitement et sans engagement au 01 48 23 71 95.</p>
      <p class="advice" style="top:251px">Nous vous accueillons dans nos bureaux au 8, rue des Tanneurs - 75003 Paris Un conseiller se déplace chez vous<br>Un conseiller vous appel pour discuter ensemble de votre projet</p>
      <p class="advice" style="top:312px">Nos conseillers sont à votre disposition du lundi au vendredi de 9h à 19h*<br>*Nos conseillers peuvent également vous accueillir le samedi de 10h à 15h si nécessaire</p>
      <p class="folio">LOI BRESSAUTINIÉ // 13</p>
    </section>
  </div>
</body>
</html>
```